ZEPRILO.COM is a premium domain sales company. Our competitors are companies like vastplots.example, getparcels.example, peerwords.example. Our current site is at www.zeprilos.example.

We want to have the ability to search for domains, to highlight special offers and have some testimonials on the index page.

The logo for the site is attached.

Please be sure that the order form fits on the screen without scrolling the page. I want the entire form, including the submit button to fit without any page scrolling.

Delivered product - INDEX PAGE, ORDER FORM AND CONTENT PAGE PSDs.

Target Market(s)

Small to Medium business professionals

Industry/Entity Type

It Company

Requirements
Must have
• 1. List of domains for sale
2. Simple search box with button to run the search
3. link for advanced search
4. testimonial area. Note - this can be a small box where a different testimonial is displayed on each page load.
Nice to have
• Would like the site to have some white space. Don't want a heavily packed website. Give it an "airy" feel.

```html
<!DOCTYPE html>
<html lang="en">
<head>
<meta charset="utf-8">
<title>Zeprilo.com — Find Your Domain</title>
<link href="https://fonts.googleapis.com/css2?family=Open+Sans:ital,wght@0,400;0,600;0,700;1,400&display=swap" rel="stylesheet">
<style>
:root{
  --blue:#1565c0;
  --blue-dark:#0d4f9e;
  --blue-text:#1a5bb0;
  --green:#7db544;
  --green-dark:#2f7d1e;
  --grey-bg:#e6e6e6;
  --grey-line:#d6d6d6;
  --text:#333;
  --footer:#555;
  --red:#e2473f;
}
*{box-sizing:border-box;margin:0;padding:0}
html,body{width:1200px;height:1084px;overflow:hidden}
body{font-family:"Open Sans",Arial,sans-serif;color:var(--text);background:#fff;position:relative}
a{color:inherit;text-decoration:none}

.site-header{position:absolute;left:0;top:0;width:1200px;height:135px;background:linear-gradient(#fff,#ececec)}
.logo{position:absolute;left:133px;top:38px;display:flex;align-items:center;gap:7px;font-size:29px;font-weight:700;color:var(--blue-dark);letter-spacing:-0.5px}
.logo-dot{width:12px;height:12px;border-radius:50%;background:var(--green-dark)}
.help{position:absolute;right:129px;top:15px;text-align:right;line-height:1.3}
.help-title{font-size:17px;font-weight:700;color:var(--blue-dark)}
.help-line{font-size:13.5px;color:#444}
.help-phone{font-size:21px;font-weight:600;color:var(--blue-dark);margin-top:1px}
.main-nav{position:absolute;left:130px;top:94px;width:620px;height:40px;background:linear-gradient(var(--blue),var(--blue-dark));border-radius:4px 4px 0 0;display:flex;align-items:center;padding-left:24px}
.main-nav a{color:#fff;font-size:12.5px;text-transform:uppercase}
.main-nav a:nth-child(1){margin-right:47px}
.main-nav a:nth-child(2){margin-right:43px}
.main-nav a:nth-child(3){margin-right:42px}
.main-nav a:nth-child(4){margin-right:41px}
.main-nav a:nth-child(5){margin-right:46px}

.hero{position:absolute;left:0;top:135px;width:1200px;height:357px;background:radial-gradient(ellipse 520px 300px at 560px 170px,#8cc24a,#5fa534 55%,#2f7d1e)}
.hero h1{position:absolute;left:171px;top:38px;font-size:31px;font-weight:600;color:#fff}
.hero .sub{position:absolute;left:171px;top:80px;font-size:14px;font-weight:600;color:#fff}
.search-box{position:absolute;left:171px;top:107px;width:463px;height:53px;background:#fff;border:2px solid #dcdcdc;border-radius:5px;padding:0 13px;display:flex;align-items:center;font-size:14px;color:#bbb;font-weight:600}
.adv-link{position:absolute;left:389px;top:176px;font-size:15px;font-weight:600;color:#fff;text-decoration:underline}
.search-btn{position:absolute;left:530px;top:167px;width:102px;height:41px;background:linear-gradient(#2a7ad6,var(--blue-dark));border:1px solid #0b4080;border-radius:4px;color:#fff;font-size:14px;font-weight:600;display:flex;align-items:center;justify-content:center}
.slide-dots{position:absolute;left:130px;top:316px;display:flex;gap:4px}
.slide-dots span{width:17px;height:17px;border-radius:50%;background:#9acd5c;opacity:.75}
.slide-dots span:first-child{background:#b6e36f;opacity:1}
.hero-photo{position:absolute;left:695px;top:5px;width:295px;height:352px;border-radius:120px 120px 0 0;background:linear-gradient(#cfd2d4,#e9eaeb 60%,#d9dbdd)}

.domain-panel{position:absolute;left:130px;top:530px;width:621px}
.tabs{height:52px;background:var(--grey-bg);border:1px solid var(--grey-line);border-radius:4px;font-size:15px;font-weight:600;color:#333;position:relative}
.tabs span{position:absolute;top:16px}
.tabs span:nth-child(1){left:21px}
.tabs span:nth-child(2){left:218px}
.tabs span:nth-child(3){left:429px}
.tab-pointer{position:absolute;left:80px;top:51px;width:0;height:0;border-left:10px solid transparent;border-right:10px solid transparent;border-top:10px solid var(--grey-bg)}
.table-box{margin-top:6px;height:375px;border:1px solid var(--grey-line);border-radius:4px;padding:19px 20px 0}
.domain-table{width:579px;border-collapse:collapse;font-size:12.5px}
.domain-table th{background:var(--green);color:#fff;font-size:15px;font-weight:600;text-align:left;height:36px}
.domain-table td{height:30px;border-bottom:1px solid #ddd;color:#333}
.domain-table tr:nth-child(2) td{height:36px;padding-top:6px}
.domain-table tr:last-child td{border-bottom:none}
.domain-table td:first-child,.domain-table th:first-child{padding-left:22px;width:202px}
.domain-table .c2{width:155px}
.domain-table .c3{width:133px}
.buy{color:var(--blue-text);font-weight:600;display:flex;align-items:center;justify-content:space-between;padding-right:6px}
.buy i{width:11px;height:11px;border-radius:50%;background:var(--red);display:inline-block;position:relative}
.buy i::after{content:"";position:absolute;left:3px;top:3.5px;width:3px;height:3px;border-right:1.5px solid #fff;border-top:1.5px solid #fff;transform:rotate(45deg)}

.side-card{position:absolute;left:769px;width:302px;border:1px solid var(--grey-line);border-radius:4px;background:linear-gradient(#f2f2f2,#fff 40px);padding:0 14px}
.side-card h2{font-size:17px;font-weight:600;color:#333;height:36px;line-height:38px;border-bottom:1px solid #ddd}
.safe{top:530px;height:238px}
.trust-list{list-style:none;margin-top:15px}
.trust-list li{display:flex;gap:9px;height:46px}
.trust-list svg{flex:none;margin-top:2px}
.trust-list a{display:block;font-family:Arial,sans-serif;font-size:14px;line-height:17px;font-weight:700;color:var(--blue-text);text-decoration:underline}
.trust-list p{font-family:Arial,sans-serif;font-size:12px;line-height:16px;color:#111}
.testimonials{top:781px;height:182px}
.arrows{position:absolute;right:14px;top:14px;display:flex;gap:3px}
.quote{font-size:12.2px;font-style:italic;color:#555;line-height:20px;margin-top:9px;letter-spacing:-0.15px;position:relative}
.quote-mark{display:inline-block;width:38px;height:14px;position:relative;vertical-align:top}
.quote-mark::before{content:"\201C";position:absolute;left:0;top:-12px;font-size:48px;line-height:48px;color:#ccc;font-style:normal}
.author{text-align:right;font-size:12.5px;margin-top:6px;line-height:18px}
.author b{display:block;color:var(--blue-text);font-weight:600}
.author em{color:#5c9e2a}

.site-footer{position:absolute;left:0;top:981px;width:1200px;height:103px;background:var(--footer)}
.footer-nav{position:absolute;left:130px;top:26px;font-size:12.5px;color:#fff}
.footer-nav span{margin:0 4px;color:#ddd}
.copyright{position:absolute;left:130px;top:57px;font-size:12.5px;color:#bbb}
.social{position:absolute;left:924px;top:42px;display:flex;gap:9px}
.social span{width:30px;height:30px;border-radius:4px}
</style>
</head>
<body>
<header class="site-header">
  <div class="logo"><span class="logo-dot"></span>ZEPRILO.COM</div>
  <div class="help">
    <div class="help-title">Questions?</div>
    <div class="help-line">We’re here to help! Call today</div>
    <div class="help-phone">1-55-501-0142</div>
  </div>
  <nav class="main-nav">
    <a href="#">Home</a><a href="#">About Us</a><a href="#">Categories</a><a href="#">Testimonials</a><a href="#">FAQ</a><a href="#">Contact Us</a>
  </nav>
</header>

<section class="hero">
  <h1>Find Your Domain</h1>
  <p class="sub">You can find the best name for your business...</p>
  <div class="search-box">ENTER DOMIAN NAME......</div>
  <a class="adv-link" href="#">Advanced Search</a>
  <div class="search-btn">SEARCH</div>
  <div class="slide-dots"><span></span><span></span><span></span><span></span></div>
  <div class="hero-photo" role="img" aria-label="Photo of a smiling businesswoman in a light grey shirt with arms crossed"></div>
</section>

<section class="domain-panel">
  <div class="tabs"><span>Featured Domains</span><span>Domain Categories</span><span>Daily Domain Deals</span><i class="tab-pointer"></i></div>
  <div class="table-box">
    <table class="domain-table">
      <tr><th>Domain</th><th class="c2">Category</th><th class="c3">Price</th><th>Option</th></tr>
      <tr><td>LarkHollow.example</td><td>Hunting</td><td>$54,000</td><td><a class="buy" href="#">Buy Now<i></i></a></td></tr>
      <tr><td>Quillora.example</td><td>All</td><td>$17,950</td><td><a class="buy" href="#">Buy Now<i></i></a></td></tr>
      <tr><td>SteepVenture.example</td><td>Extreme Sports</td><td>$15,500</td><td><a class="buy" href="#">Buy Now<i></i></a></td></tr>
      <tr><td>PlotTrellis.example</td><td>Fixtures</td><td>$5,095</td><td><a class="buy" href="#">Buy Now<i></i></a></td></tr>
      <tr><td>BlockSignal.example</td><td>Marketing</td><td>$5,390</td><td><a class="buy" href="#">Buy Now<i></i></a></td></tr>
      <tr><td>PaddleRally.example</td><td>Ping Pong</td><td>$5,295</td><td><a class="buy" href="#">Buy Now<i></i></a></td></tr>
      <tr><td>SilverVeil.example</td><td>Weddings</td><td>$5,595</td><td><a class="buy" href="#">Buy Now<i></i></a></td></tr>
      <tr><td>BannerReason.example</td><td>Equestrian</td><td>$5,390</td><td><a class="buy" href="#">Buy Now<i></i></a></td></tr>
      <tr><td>EncoreLedger.example</td><td>Rock and Pop</td><td>$5,390</td><td><a class="buy" href="#">Buy Now<i></i></a></td></tr>
      <tr><td>SandAtHome.example</td><td>Remodeling</td><td>$7,095</td><td><a class="buy" href="#">Buy Now<i></i></a></td></tr>
    </table>
  </div>
</section>

<aside class="side-card safe">
  <h2>Safe and Secure</h2>
  <ul class="trust-list">
    <li><svg width="23" height="23" viewBox="0 0 23 23"><circle cx="11.5" cy="11.5" r="11" fill="#6aa832"/><path d="M6 12l4 4 7-8" stroke="#fff" stroke-width="2.5" fill="none"/></svg><div><a href="#">Service you can trust</a><p>Servicing thousands of clients since 2005.</p></div></li>
    <li><svg width="23" height="23" viewBox="0 0 23 23"><ellipse cx="12" cy="9" rx="10" ry="7" fill="#f08a1c"/><ellipse cx="9" cy="14" rx="8" ry="5.5" fill="#e2473f"/></svg><div><a href="#">Testimonials</a><p>Read client testimonials.</p></div></li>
    <li><svg width="23" height="23" viewBox="0 0 23 23"><path d="M11.5 1l3.2 6.6 7.2 1-5.2 5 1.3 7.2-6.5-3.4-6.5 3.4 1.3-7.2-5.2-5 7.2-1z" fill="#f2a91c"/></svg><div><a href="#">100% Satisfaction Guaranteed</a><p>Your satisfaction is our priority!</p></div></li>
    <li><svg width="23" height="23" viewBox="0 0 23 23"><circle cx="11.5" cy="11.5" r="8" fill="#fff" stroke="#d33" stroke-width="5" stroke-dasharray="6.28 6.28"/><circle cx="11.5" cy="11.5" r="10.5" fill="none" stroke="#bbb" stroke-width="1"/></svg><div><a href="#">Support Center</a><p>Have a question or comment?</p></div></li>
  </ul>
</aside>

<aside class="side-card testimonials">
  <h2>Testimonials</h2>
  <div class="arrows">
    <svg width="17" height="17" viewBox="0 0 17 17"><circle cx="8.5" cy="8.5" r="8.5" fill="#111"/><path d="M12 8.5H5M7.5 6L5 8.5 7.5 11" stroke="#fff" stroke-width="1.4" fill="none"/></svg>
    <svg width="17" height="17" viewBox="0 0 17 17"><circle cx="8.5" cy="8.5" r="8.5" fill="#111"/><path d="M5 8.5h7M9.5 6L12 8.5 9.5 11" stroke="#fff" stroke-width="1.4" fill="none"/></svg>
  </div>
  <p class="quote"><span class="quote-mark"></span>They were great with response time they contacted me through email and phone in a timely manner to inform me that the domain was available for purchase. There were no ...</p>
  <p class="author"><b>Username</b><em>Websitename</em></p>
</aside>

<footer class="site-footer">
  <nav class="footer-nav"><a href="#">Home</a><span>|</span><a href="#">About</a><span>|</span><a href="#">Privacy</a><span>|</span><a href="#">Terms &amp; Conditions</a><span>|</span><a href="#">Testimonials</a></nav>
  <p class="copyright">Copyright © 2013 Zeprilos. All rights reserved.</p>
  <div class="social" aria-label="Social links">
    <span style="background:#3b5a9a"></span><span style="background:#5cc4e8"></span><span style="background:#1e7ab8"></span><span style="background:#f08a1c"></span>
  </div>
</footer>
</body>
</html>
```